Website Design for Australian Vocational Education organisation

A website for an Educational organisation. A responsive design that works well on a laptop desktop or a mobile phone. Is easy to navigate. Be able to start small and add new pages and features at a later stage.
Requires the logo, the name of company, home page with hero shots, enquiry form that forwards to a specified email address
links to social media, home page. We need a home page, and two more templates for sub pages.
Must not be a typical common design.

current website www.qlmv.edu.au
this needs to look different. logo should remain the same.

Target Market(s)

across age groups from 18-70. so must be inutitive. some will be tech savvy and others not.

Industry/Entity Type

Education

Coding

Coded - Design and coding required

Colors

Designer to choose colors to be used in the design.

Requirements
Must have
• responsive design, video, photo gallery, hero image, social media links, news feed, calendar, shopping cart, enquiry form
Nice to have
• Sample website
• www.brightpathskills.com.au
• but should not be similar to this. it must look different. the sample is to give an idea on the various pages and links that will be required

```html
<!DOCTYPE html>
<html lang="en">
<head>
<meta charset="utf-8">
<title>Kestrel Academy of Applied Skills</title>
<link href="https://fonts.googleapis.com/css2?family=Quicksand:wght@500;600;700&family=Poppins:wght@400;500;600&display=swap" rel="stylesheet">
<style>
:root{
  --red:#e51d2e;
  --navy:#212c65;
  --navy-dark:#1a2456;
  --sky:#3db7f4;
  --sky-soft:#cdeefd;
  --ink:#3a3f55;
  --muted:#6b7085;
  --line:#ececf1;
  --white:#ffffff;
}
*{margin:0;padding:0;box-sizing:border-box}
html,body{width:1200px;height:3214px;overflow:hidden;background:var(--white)}
body{position:relative;font-family:"Poppins",sans-serif;color:var(--ink)}
.abs{position:absolute}
h1,h2,h3,.brand-name{font-family:"Quicksand",sans-serif}

/* header */
.hero-shape{left:0;top:0}
.brand{display:flex;align-items:center;gap:10px}
.brand-mark{width:44px;height:44px;background:var(--navy)}
.brand-name{font-weight:700;font-size:13px;line-height:1.15;color:var(--navy);text-transform:uppercase;width:130px}
.nav-link{top:55px;font-size:10.5px;font-weight:500;color:var(--white);text-decoration:none;text-transform:uppercase;letter-spacing:.2px;white-space:nowrap}
.nav-link.active{border-bottom:2px solid var(--red);padding-bottom:5px}
.btn-apply{left:934px;top:49px;width:96px;height:27px;background:var(--red);color:var(--white);border-radius:3px;font-size:10.5px;font-weight:500;display:flex;align-items:center;justify-content:center;text-transform:uppercase;white-space:nowrap}
.swatch{width:27px;height:14px}
.swatch-label{font-size:14px;letter-spacing:1px;font-family:"Quicksand",sans-serif;font-weight:600}

.hero-kicker{left:156px;top:200px;color:var(--red);font-size:20px;font-weight:600}
.hero-title{left:156px;top:230px;color:var(--navy);font-size:28px;font-weight:600;white-space:nowrap}
.hero-text{left:156px;top:294px;width:305px;font-size:11.5px;line-height:1.7;color:var(--muted)}
.btn{height:32px;border-radius:2px;color:var(--white);font-size:11px;display:flex;align-items:center;justify-content:center;text-transform:uppercase;font-weight:500}
.btn-red{background:var(--red)}
.btn-navy{background:var(--navy)}

/* features */
.feature{width:276px;height:127px;border:1px solid var(--line);box-shadow:0 4px 14px rgba(33,44,101,.07);background:var(--white);display:flex;gap:12px;padding:26px 14px}
.feature h3{font-size:14px;color:var(--navy);font-weight:600;margin-bottom:6px;white-space:nowrap}
.feature p{font-size:10px;line-height:1.55;color:var(--muted)}
.feature svg{flex:none}

/* welcome */
.section-title{font-size:28px;font-weight:600;color:var(--navy);white-space:nowrap}
.welcome-text{left:568px;top:1180px;width:385px;font-size:10.5px;line-height:1.75;color:var(--muted)}
.stat{font-family:"Quicksand",sans-serif}
.stat b{display:block;color:var(--red);font-size:22px;font-weight:600}
.stat span{display:block;color:var(--navy);font-size:11px;font-weight:600;line-height:1.35;margin-top:6px}

/* courses */
.course{height:203px;display:flex;background:var(--white);box-shadow:0 4px 18px rgba(33,44,101,.09)}
.course .pic{width:216px;height:203px;flex:none}
.course .body{padding:32px 24px}
.course h3{font-size:18px;color:var(--navy);font-weight:600;margin-bottom:22px;white-space:nowrap}
.course p{font-size:10.5px;line-height:1.7;color:var(--muted);width:250px}
.course .more{display:block;margin-top:26px;font-size:10px;font-weight:600;color:var(--red);text-transform:uppercase}

/* testimonials */
.center{left:0;width:1200px;text-align:center}
.subtitle{font-size:12.5px;color:var(--ink)}
.testimonial{top:2310px;height:214px;width:438px;background:var(--white);box-shadow:0 4px 18px rgba(33,44,101,.09);text-align:center;padding-top:18px}
.avatar{width:68px;height:68px;border-radius:50%;margin:0 auto 10px}
.testimonial h3{font-size:14px;color:var(--navy);font-weight:600}
.testimonial .role{font-size:10.5px;color:var(--red);margin-top:4px}
.testimonial p{font-size:10px;line-height:1.7;color:var(--muted);margin:14px auto 0;width:395px}

/* newsletter */
.signup{left:418px;top:2741px;width:382px;height:44px;border-radius:22px;box-shadow:0 3px 14px rgba(33,44,101,.12);background:var(--white)}
.signup span{position:absolute;left:22px;top:14px;font-size:11px;color:#a5a8b6}
.signup b{position:absolute;right:0;top:0;width:114px;height:44px;border-radius:22px;background:var(--red);color:var(--white);font-size:10.5px;font-weight:600;display:flex;align-items:center;justify-content:center;text-transform:uppercase}

/* footer */
.footer{left:0;top:2882px;width:1200px;height:285px;background:var(--navy)}
.footer-bar{left:0;top:3167px;width:1200px;height:47px;background:var(--navy-dark)}
.footer .brand-name{color:var(--white)}
.footer .brand-mark{background:var(--white)}
.fcol h4{font-family:"Quicksand",sans-serif;font-size:12px;font-weight:700;color:var(--white);text-transform:uppercase;margin-bottom:20px}
.fcol li{list-style:none;font-size:11px;color:#d5d8e8;line-height:22.7px;white-space:nowrap}
.contact li{list-style:none;display:flex;align-items:center;gap:12px;font-size:11px;color:#d5d8e8;height:23px;white-space:nowrap}
.copyright{left:167px;top:3183px;font-size:10px;color:#d5d8e8;text-transform:uppercase;letter-spacing:.3px;white-space:nowrap}
.social{left:937px;top:3182px;display:flex;gap:13px}
.social i{display:block;width:12px;height:12px;background:var(--white);border-radius:2px}
</style>
</head>
<body>

<!-- hero background -->
<svg class="abs hero-shape" width="1200" height="600" viewBox="0 0 1200 600" aria-hidden="true">
  <path d="M450 0 H1200 V448 Q1200 470 1180 478 L620 578 Q560 590 548 530 L460 90 Q450 40 450 0 Z" fill="var(--sky)"/>
</svg>

<div class="abs brand" style="left:167px;top:32px">
  <div class="brand-mark"></div>
  <div class="brand-name">Kestrel Academy of Applied Skills</div>
</div>
<nav>
  <a class="abs nav-link active" style="left:507px">Home</a>
  <a class="abs nav-link" style="left:567px">About</a>
  <a class="abs nav-link" style="left:633px">Courses</a>
  <a class="abs nav-link" style="left:712px">Students</a>
  <a class="abs nav-link" style="left:795px">Blog</a>
  <a class="abs nav-link" style="left:852px">Contact</a>
</nav>
<div class="abs btn-apply">Apply Online</div>

<div class="abs swatch" style="left:313px;top:94px;background:var(--red)"></div>
<div class="abs swatch-label" style="left:313px;top:113px;color:var(--red)">E51D2E</div>
<div class="abs swatch" style="left:386px;top:94px;background:var(--navy)"></div>
<div class="abs swatch-label" style="left:386px;top:113px;color:var(--navy)">212C65</div>

<div class="abs hero-kicker">meet your friends</div>
<h1 class="abs hero-title">Make Your Tomorrow</h1>
<p class="abs hero-text">Lorem ipsum dolor sit amet, consectetur adipiscing elit. Donec et velit ipsum. Fusce luctus eget ex nec vehicula. Phasellus eu ultrices metus, feugiat porta nulla.</p>
<div class="abs btn btn-red" style="left:163px;top:387px;width:141px">Know More</div>
<div class="abs btn btn-navy" style="left:319px;top:387px;width:141px">View Courses</div>

<div class="abs" role="img" aria-label="Photo of a student pouring milk at a café table" style="left:656px;top:206px;width:466px;height:466px;border-radius:50%;border:5px solid #eef1f6;background:radial-gradient(circle at 40% 40%,#5a6f8c,#2f3b52 70%)"></div>
<div class="abs" role="img" aria-label="Photo of two smiling students studying outdoors" style="left:559px;top:195px;width:244px;height:244px;border-radius:50%;border:4px solid var(--white);background:linear-gradient(140deg,#5e8a4a,#b9a68a 60%,#7fa3c8)"></div>

<!-- features -->
<div class="abs feature" style="left:161px;top:767px">
  <svg width="48" height="48" viewBox="0 0 52 52" aria-hidden="true"><g fill="var(--navy)"><circle cx="14" cy="12" r="5"/><circle cx="26" cy="10" r="6"/><circle cx="38" cy="12" r="5"/><rect x="8" y="19" width="12" height="24" rx="3"/><rect x="19" y="18" width="14" height="28" rx="3"/><rect x="32" y="19" width="12" height="24" rx="3"/></g></svg>
  <div><h3>Hospitality Management</h3><p>Lorem ipsum dolor sit amet esta di maria nuno valenica</p></div>
</div>
<div class="abs feature" style="left:463px;top:767px">
  <svg width="48" height="48" viewBox="0 0 52 52" aria-hidden="true"><g fill="var(--navy)"><circle cx="20" cy="12" r="6"/><circle cx="32" cy="12" r="6"/><rect x="16" y="12" width="20" height="10" rx="2"/><path d="M12 32 L40 46 M40 32 L12 46" stroke="var(--navy)" stroke-width="4" stroke-linecap="round"/></g></svg>
  <div><h3>Commercial Cookery</h3><p>Lorem ipsum dolor sit amet esta di maria nuno valenica</p></div>
</div>
<div class="abs feature" style="left:763px;top:767px">
  <svg width="48" height="48" viewBox="0 0 52 52" aria-hidden="true"><g fill="var(--navy)"><circle cx="12" cy="16" r="5"/><circle cx="26" cy="12" r="7"/><circle cx="40" cy="16" r="5"/><path d="M4 42 Q4 24 12 24 Q20 24 20 42 Z"/><path d="M15 46 Q15 22 26 22 Q37 22 37 46 Z"/><path d="M32 42 Q32 24 40 24 Q48 24 48 42 Z"/></g></svg>
  <div><h3>Leadership Management</h3><p>Lorem ipsum dolor sit amet esta di maria nuno valenica</p></div>
</div>

<!-- welcome -->
<svg class="abs" style="left:0;top:915px" width="530" height="490" viewBox="0 0 530 490">
  <path d="M0 60 L330 220 Q520 310 420 440 Q380 490 300 460 L0 315 Z" fill="var(--sky-soft)"/>
  <path role="img" aria-label="Photo of hands working on a laptop at a wooden desk" d="M0 0 L330 200 Q500 300 410 410 Q370 450 300 420 L0 295 Z" fill="#6a5a4a"/>
</svg>
<h2 class="abs section-title" style="left:568px;top:1110px">Welcome to our Courses</h2>
<p class="abs welcome-text">Lorem ipsum dolor sit amet, consectetur adipiscing elit. Donec augue odio, auctor ut feugiat tristique, venenatis id erat. Mauris ut ligula ut elit pellentesque tristique ut eu diam. Sed mi velit, mattis commodo ligula sit amet, ultrices aliquet nisi. Morbi gravida dolor eget turpis elementum.</p>
<div class="abs stat" style="left:568px;top:1288px"><b>05</b><span>Leadership<br>Management</span></div>
<div class="abs stat" style="left:701px;top:1288px"><b>10</b><span>Hospital<br>Management</span></div>
<div class="abs stat" style="left:836px;top:1288px"><b>15</b><span>Commercial<br>Cookery</span></div>

<!-- popular courses -->
<h2 class="abs section-title center" style="top:1520px">Popular Courses</h2>
<div class="abs course" style="left:174px;top:1620px;width:538px">
  <div class="pic" role="img" aria-label="Photo of guests in a dimly lit restaurant" style="background:linear-gradient(135deg,#3a3f48,#1e2630)"></div>
  <div class="body"><h3>Hospitality Management</h3><p>Lorem ipsum dolor sit amet, consectetur adipiscing elit. Donec augue odio, auctor ut feugiat tristique, venenatis id erat.</p><span class="more">Read More</span></div>
</div>
<div class="abs course" style="left:493px;top:1870px;width:538px">
  <div class="pic" role="img" aria-label="Photo of a chef at a stack of plates in a commercial kitchen" style="background:linear-gradient(135deg,#2e2a28,#a2856a)"></div>
  <div class="body"><h3>Commercial Cookery</h3><p>Lorem ipsum dolor sit amet, consectetur adipiscing elit. Donec augue odio, auctor ut feugiat tristique, venenatis id erat.</p><span class="more">Read More</span></div>
</div>

<!-- testimonials -->
<h2 class="abs section-title center" style="top:2174px">Testimonials</h2>
<p class="abs subtitle center" style="top:2232px">what clients/students says about our courses</p>
<div class="abs testimonial" style="left:-114px">
  <div class="avatar" role="img" aria-label="Portrait of a former student" style="background:#b07a52"></div>
  <h3>Maren Holloway</h3><div class="role">Ex Student/ Restaurant Owner</div>
  <p>Donec eu congue urna. Morbi fermentum, purus eu volutpat malesuada, urna lacus pellentesque libero, eu gravida sapien nibh eget sapien.</p>
</div>
<div class="abs testimonial" style="left:377px">
  <div class="avatar" role="img" aria-label="Portrait of a current student" style="background:#e0b070"></div>
  <h3>Priya Lowell</h3><div class="role">Student</div>
  <p>Donec eu congue urna. Morbi fermentum, purus eu volutpat malesuada, urna lacus pellentesque libero, eu gravida sapien nibh eget sapien.</p>
</div>
<div class="abs testimonial" style="left:866px">
  <div class="avatar" role="img" aria-label="Portrait of a current student" style="background:#c89a7c"></div>
  <h3>Tomas Rendell</h3><div class="role">Student</div>
  <p>Donec eu congue urna. Morbi fermentum, purus eu volutpat malesuada, urna lacus pellentesque libero, eu gravida sapien nibh eget sapien.</p>
</div>

<!-- newsletter -->
<h2 class="abs section-title center" style="top:2602px">Newsletter</h2>
<p class="abs subtitle center" style="top:2658px">To get update on new course, certificate etc. subcribe us</p>
<div class="abs signup"><span>Type your email id</span><b>Subscribe</b></div>

<!-- footer -->
<footer class="abs footer">
  <svg class="abs" style="left:0;top:0" width="1200" height="285" aria-hidden="true"><path d="M0 0 H200 L0 120 Z" fill="rgba(255,255,255,.03)"/><path d="M1200 285 H880 L1200 130 Z" fill="rgba(255,255,255,.04)"/></svg>
  <div class="abs brand" style="left:171px;top:64px">
    <div class="brand-mark"></div>
    <div class="brand-name">Kestrel Academy of Applied Skills</div>
  </div>
  <ul class="abs contact" style="left:171px;top:146px">
    <li><svg width="12" height="12" viewBox="0 0 12 12"><rect x="1" y="3" width="10" height="7" fill="none" stroke="#fff"/></svg>18 Wattle Grove, Northbridge ACT 2690</li>
    <li><svg width="12" height="12" viewBox="0 0 12 12"><circle cx="6" cy="6" r="5" fill="none" stroke="#fff"/><path d="M6 3V6H8" stroke="#fff" fill="none"/></svg>Mon - Fri 8.30 AM - 04.30 PM</li>
    <li><svg width="12" height="12" viewBox="0 0 12 12"><path d="M2 1 L5 1 L6 4 L4 5 Q5 7 7 8 L8 6 L11 7 L11 10 Q6 11 1 4 Z" fill="#fff"/></svg>+61 400 555 182</li>
    <li><svg width="12" height="12" viewBox="0 0 12 12"><rect x="1" y="2" width="10" height="8" fill="none" stroke="#fff"/><path d="M1 2 L6 7 L11 2" stroke="#fff" fill="none"/></svg>info@qlmv.edu.au</li>
  </ul>
  <div class="abs fcol" style="left:489px;top:72px"><h4>Home</h4><ul><li>About us</li><li>Our Vision</li><li>Our Mission</li><li>Contact Us</li><li>Apply Online</li></ul></div>
  <div class="abs fcol" style="left:697px;top:72px"><h4>Courses</h4><ul><li>Chef</li><li>Cookery</li><li>Hotel Service</li><li>Leadership Management</li><li>Hospital Management</li><li>Commercial Cookery</li></ul></div>
  <div class="abs fcol" style="left:928px;top:72px"><h4>Quick Info</h4><ul><li>Fees</li><li>Terms &amp; Conditions</li><li>Privacy Policy</li><li>Certificates</li><li>Job Options</li></ul></div>
</footer>
<div class="abs footer-bar"></div>
<div class="abs copyright">2018 KAAS. Copyright © Kestrel Academy of Applied Skills Pty Ltd | ACN: 000 111 222 | RTO: 90000</div>
<div class="abs social" aria-label="Social media links"><i></i><i></i><i></i><i></i></div>

</body>
</html>
```